依頼概要
初めまして。よろしくお願いいたします。

依頼内容
※エコー(赤ちゃん)ポスターのデザイン依頼

※エコー写真をスキャンして嵌め込みますので、そちらを想定したテンプレート型のポスターデザインをお願いいたします。

※エコーの枚数は3・6・9枚の何れかでお願いいたします。

※子供の名前 身長体重 出産時間 等

ポスターデザインのイメージや雰囲気は
デザイナー様各々におまかせしております。

```html
<!DOCTYPE html>
<html lang="en">
<head>
<meta charset="UTF-8">
<title>Birth Poster – SAKURA</title>
<link rel="stylesheet" href="https://fonts.googleapis.com/css2?family=Nunito:wght@800;900&display=swap">
<style>
  :root {
    --pink: #ec5b9c;
    --pink-soft: #f6b8d4;
    --bg-top: #f8cfe3;
    --bg-bottom: #fdf4a8;
    --white: #ffffff;
    --ink: #3a3a3a;
    --echo-dark: #1c1c1c;
    --echo-mid: #6b6b6b;
    --illus-warm: #f4b860;
    --illus-pink: #f7a9c6;
  }
  * { margin: 0; padding: 0; box-sizing: border-box; }
  html, body { width: 846px; height: 1200px; overflow: hidden; }
  body { font-family: "Nunito", sans-serif; }

  .poster {
    position: relative;
    width: 846px;
    height: 1200px;
    background: linear-gradient(180deg, var(--bg-top) 0%, #fbe3d2 45%, var(--bg-bottom) 100%);
    overflow: hidden;
  }

  .headline {
    position: absolute;
    top: 14px; left: 0; width: 100%;
    text-align: center;
    font-weight: 900;
    font-size: 44px;
    letter-spacing: 1px;
    color: var(--pink);
  }

  .photo-frame {
    position: absolute;
    left: 222px; top: 78px;
    width: 456px; height: 346px;
    background: var(--white);
    box-shadow: 0 4px 10px rgba(0,0,0,0.12);
  }
  .photo-frame .tape {
    position: absolute;
    left: 140px; top: -14px;
    width: 120px; height: 34px;
    background: rgba(246,184,212,0.85);
    transform: rotate(-3deg);
  }
  .baby-photo {
    position: absolute;
    left: 26px; top: 24px;
    width: 404px; height: 298px;
    background: linear-gradient(135deg, #e8e4ea 0%, #d7cfd6 50%, #c9d3e6 100%);
  }

  .illus {
    position: absolute;
    border-radius: 40%;
  }
  .illus-bear { left: 50px; top: 238px; width: 160px; height: 186px; background: linear-gradient(180deg, var(--illus-warm), #f6cc7d); }
  .illus-rabbit { left: 660px; top: 226px; width: 160px; height: 198px; background: linear-gradient(180deg, var(--illus-pink), #f9c4d8); }
  .illus-squirrel { left: 42px; top: 660px; width: 128px; height: 140px; background: linear-gradient(180deg, #f2ad55, #f6c879); }
  .illus-dog { left: 690px; top: 664px; width: 130px; height: 130px; background: linear-gradient(180deg, #f1c070, #f6d496); }

  .date-band {
    position: absolute;
    left: 72px; top: 438px;
    width: 702px; height: 72px;
    background: var(--pink);
    color: var(--white);
    font-weight: 900;
    font-size: 56px;
    line-height: 72px;
    text-align: center;
    letter-spacing: 1px;
  }

  .baby-name {
    position: absolute;
    top: 512px; left: 0; width: 100%;
    text-align: center;
    font-weight: 900;
    font-size: 136px;
    line-height: 150px;
    color: var(--pink);
    letter-spacing: 2px;
  }

  .details {
    position: absolute;
    left: 180px; top: 680px;
    width: 490px;
    display: grid;
    grid-template-columns: 1fr 1fr;
    row-gap: 2px;
    color: var(--ink);
  }
  .detail { white-space: nowrap; font-weight: 900; }
  .detail .label { font-size: 19px; margin-right: 8px; }
  .detail .value { font-size: 40px; }

  .echo-grid {
    position: absolute;
    left: 40px; top: 800px;
    width: 768px;
    display: grid;
    grid-template-columns: repeat(3, 228px);
    column-gap: 42px;
    row-gap: 48px;
  }
  .echo-slot {
    position: relative;
    height: 144px;
    background: radial-gradient(ellipse at 50% 60%, var(--echo-mid) 0%, #3a3a3a 45%, var(--echo-dark) 80%);
    border: 4px solid var(--white);
    box-shadow: 0 2px 6px rgba(0,0,0,0.2);
  }
  .arrow {
    position: absolute;
    width: 20px; height: 24px;
  }
</style>
</head>
<body>
<main class="poster">
  <h1 class="headline">♥ THANK YOU BEING BORN ♥</h1>

  <div class="photo-frame">
    <div class="baby-photo" role="img" aria-label="Photograph of the newborn baby sleeping"></div>
    <div class="tape"></div>
  </div>

  <div class="illus illus-bear" role="img" aria-label="Illustration of a cheerful bear"></div>
  <div class="illus illus-rabbit" role="img" aria-label="Illustration of a pink rabbit"></div>
  <div class="illus illus-squirrel" role="img" aria-label="Illustration of a squirrel"></div>
  <div class="illus illus-dog" role="img" aria-label="Illustration of a puppy"></div>

  <div class="date-band">AUG.30.2020.8:00PM</div>
  <div class="baby-name">SAKURA</div>

  <div class="details">
    <div class="detail"><span class="label">FATHER</span><span class="value">TAKU</span></div>
    <div class="detail"><span class="label">MOTHER</span><span class="value">NAOMI</span></div>
    <div class="detail"><span class="label">WEIGHT</span><span class="value">3210g</span></div>
    <div class="detail"><span class="label">HEIGHT</span><span class="value">51.5cm</span></div>
  </div>

  <section class="echo-grid">
    <div class="echo-slot" role="img" aria-label="Ultrasound scan 1"></div>
    <div class="echo-slot" role="img" aria-label="Ultrasound scan 2"></div>
    <div class="echo-slot" role="img" aria-label="Ultrasound scan 3"></div>
    <div class="echo-slot" role="img" aria-label="Ultrasound scan 4"></div>
    <div class="echo-slot" role="img" aria-label="Ultrasound scan 5"></div>
    <div class="echo-slot" role="img" aria-label="Ultrasound scan 6"></div>
  </section>

  <svg class="arrow" style="left:280px;top:862px" viewBox="0 0 20 24"><polygon points="0,0 20,12 0,24" fill="#ec5b9c"/></svg>
  <svg class="arrow" style="left:550px;top:862px" viewBox="0 0 20 24"><polygon points="0,0 20,12 0,24" fill="#ec5b9c"/></svg>
  <svg class="arrow" style="left:280px;top:1054px" viewBox="0 0 20 24"><polygon points="0,0 20,12 0,24" fill="#ec5b9c"/></svg>
  <svg class="arrow" style="left:550px;top:1054px" viewBox="0 0 20 24"><polygon points="0,0 20,12 0,24" fill="#ec5b9c"/></svg>
</main>
</body>
</html>
```